Ridgeline pedal treks co

we are an electric mountain bike company in Nelson, New Zealand. We need to create flyers to have in local stores/ information centres etc for our company. you can view the website for ideas on whats required in the flyer www. ridgelinepedaltreksco.example.nz., on the website in our region and our trails gives me detail on the tracks etc available to the clients. I will attach in the brief some screen shots from the website of the content on our services packages etc . I Will also upload a couple versions of our logo.If you wish to incorporate anything else that represents nz and the Nelson region that would be fantastic. Please include all relevant contact email, facebook, instagram etc, looking for something with flare that catches the eye but also clarity on information and looks appealing. wanting DLE size double sided

Target Market(s)

international travellers/ staff parties/ group bookings/

Industry/Entity Type

Tourism

Requirements
Must have
• 1. map of nz with nelson on it. Location
• 2 info on or services
• 3. contact info
• 4. about the region
• 5. track information.
• 6 tour information.
• 7. eye catching layout.
Nice to have
• 1. information on what we offer.
• 2. nz icons etc kiwi, silver fern, southern alps, marlow reach, scenery shots

```html
<!DOCTYPE html>
<html lang="en">
<head>
<meta charset="utf-8">
<title>Ridgeline pedal treks co – DL flyer</title>
<link href="https://fonts.googleapis.com/css2?family=Oswald:wght@600;700&family=Lato:wght@300;400;700&display=swap" rel="stylesheet">
<style>
  :root{
    --stage:#a9a9ab;
    --paper:#f4f4f4;
    --ink:#1e1e1e;
    --night:#0b0f15;
    --rule:#3a3f46;
    --white:#ffffff;
    --orange:#f07a22;
    --green:#2a8a3e;
    --blue:#4a6fc0;
    --photo-sky:#cfd6dc;
    --photo-earth:#6b5a44;
  }
  *{box-sizing:border-box;margin:0;padding:0}
  html,body{width:1200px;height:1200px;overflow:hidden;background:var(--stage)}
  .canvas{position:relative;width:1200px;height:1200px}
  .panel{position:absolute;top:64px;width:512px;height:1084px;overflow:hidden}
  .panel--front{left:74px;background:linear-gradient(180deg,var(--paper) 60%,#e6e7e8 100%)}
  .panel--back{left:634px;background:var(--night);color:var(--white)}
  .tricolour{position:absolute;left:0;width:100%;height:5px;display:flex;z-index:3}
  .tricolour span{flex:1}
  .tricolour span:nth-child(1){background:var(--orange)}
  .tricolour span:nth-child(2){background:var(--green)}
  .tricolour span:nth-child(3){background:var(--blue)}
  .tricolour--top{top:0}.tricolour--bottom{bottom:0}

  .hero-photo{position:absolute;left:0;top:0;width:512px;height:440px;
    background:linear-gradient(180deg,var(--photo-sky) 0%,#9aa5ad 45%,#5d6b4c 75%,var(--photo-earth) 100%);
    clip-path:ellipse(120% 100% at 50% 0%)}
  .round{position:absolute;width:168px;height:168px;border-radius:50%;border:6px solid var(--paper);transform:translate(-50%,-50%)}
  .round--left{left:90px;top:412px;background:linear-gradient(180deg,#9fc3e4,#4d6a47)}
  .round--right{left:424px;top:412px;background:linear-gradient(180deg,#2f78c6,#3a3a36)}
  .brand-badge{position:absolute;left:256px;top:436px;width:160px;height:160px;border-radius:50%;
    background:#0c0c0c;transform:translate(-50%,-50%);display:flex;align-items:center;justify-content:center;
    font-family:'Oswald',sans-serif;font-weight:700;font-size:24px;color:var(--white);letter-spacing:1px}

  .welcome{position:absolute;left:0;top:570px;width:100%;text-align:center;white-space:nowrap;
    font-family:'Oswald',sans-serif;font-weight:700;font-size:48px;letter-spacing:-1.5px;color:var(--ink);line-height:1.1}
  .intro{position:absolute;left:0;top:638px;width:100%;text-align:center;white-space:nowrap;
    font-family:'Lato',sans-serif;font-size:24px;line-height:34.4px;color:#2b2b2b}
  .fern{position:absolute;left:170px;top:858px;width:176px;height:34px;background:linear-gradient(90deg,#1a1a1a,#666);border-radius:30px 6px 30px 6px;transform:rotate(-14deg)}
  .call{position:absolute;left:0;top:932px;width:100%;text-align:center;
    font-family:'Oswald',sans-serif;font-weight:600;font-size:33px;color:var(--ink);line-height:1.1}
  .email{position:absolute;left:0;top:975px;width:100%;text-align:center;
    font-family:'Lato',sans-serif;font-weight:700;font-size:22px;line-height:28px;color:var(--ink)}
  .web{position:absolute;left:0;top:1009px;width:100%;text-align:center;
    font-family:'Lato',sans-serif;font-weight:700;font-size:20px;line-height:26px;color:var(--ink)}

  .tours-title{position:absolute;left:0;top:42px;width:100%;text-align:center;
    font-family:'Oswald',sans-serif;font-weight:700;font-size:52px;letter-spacing:-1px;line-height:1.1}
  .tour-list{position:absolute;left:0;top:113px;width:100%;list-style:none}
  .tour{margin:0 76px;height:85.5px;text-align:center;border-bottom:2px solid var(--rule);
    font-family:'Lato',sans-serif;font-weight:300;font-size:25px;line-height:34.4px;display:flex;flex-direction:column;justify-content:center;align-items:center}
  .tour:first-child{height:80px}
  .tour:last-child{border-bottom:none}
  .tour span{white-space:nowrap}
  .region-map{position:absolute;left:29px;top:812px;width:458px;height:210px;
    background:linear-gradient(160deg,#d9c89a 0%,#b9d6e6 35%,#a9cfe3 55%,#d7caa0 75%,#9fbf7e 100%)}
  .web--back{position:absolute;left:0;top:1038px;width:100%;text-align:center;
    font-family:'Lato',sans-serif;font-weight:700;font-size:21px;line-height:28px;color:var(--white)}
</style>
</head>
<body>
<main class="canvas">
  <section class="panel panel--front">
    <div class="tricolour tricolour--top"><span></span><span></span><span></span></div>
    <div class="hero-photo" role="img" aria-label="Downhill mountain biker riding a dirt slope with alpine peaks and clouds behind"></div>
    <div class="round round--left" role="img" aria-label="Rider in hi-vis vest with an e-bike overlooking the coast"></div>
    <div class="round round--right" role="img" aria-label="Group of riders with bikes on a ridge against blue sky"></div>
    <div class="brand-badge">RIDGELINE</div>
    <h1 class="welcome">WELCOME TO RIDGELINE</h1>
    <p class="intro">We are an electric mountain bike<br>company specialising in full suspension<br>e-bike rental, guided tours and custom<br>MTB packages in the Nelson and<br>Tasman region.</p>
    <div class="fern" role="img" aria-label="Silver fern emblem"></div>
    <p class="call">CALL : 800-555-010-2040</p>
    <p class="email">Email: info@ridgelinepedaltreksco</p>
    <p class="web">www.ridgelinepedaltreksco.example.nz</p>
    <div class="tricolour tricolour--bottom"><span></span><span></span><span></span></div>
  </section>

  <section class="panel panel--back">
    <div class="tricolour tricolour--top"><span></span><span></span><span></span></div>
    <h2 class="tours-title">TOUR OPTIONS</h2>
    <ul class="tour-list">
      <li class="tour"><span>Kaiteriteri MTB Park and Marlow Reach –</span><span>Beginner/Intermediate</span></li>
      <li class="tour"><span>Rameka Trail Golden Bay –</span><span>Intermediate/Advanced</span></li>
      <li class="tour"><span>Coppermine/Third house –</span><span>Beginner/Intermmediate</span></li>
      <li class="tour"><span>Nelson Lakes –</span><span>Beginner/Intermediate/Advanced</span></li>
      <li class="tour"><span>Codgers MTB park/Fringe Hill –</span><span>Beginner/Intermediate/Advanced</span></li>
      <li class="tour"><span>Barnicoat/Involution –</span><span>Intermediate/Advanced</span></li>
      <li class="tour"><span>Richmond Hills –</span><span>Intermediate/Advanced</span></li>
      <li class="tour"><span>Sharlands –</span><span>Beginner/Intermediate/Advanced</span></li>
    </ul>
    <div class="region-map" role="img" aria-label="Topographic map of Nelson and surrounding hills with numbered trail areas"></div>
    <p class="web--back">www.ridgelinepedaltreksco.example.nz</p>
    <div class="tricolour tricolour--bottom"><span></span><span></span><span></span></div>
  </section>
</main>
</body>
</html>
```